Banner and Tablecloth for trade show

This will be a design for 2 trade show roll up banners (I've attached an image with dimensions and an example) and a simple tablecloth design (also attached with dimensions and example).
For the Tablecloth: We just need something simple with our logo, and the attached Summit Ledger certified logo.
For the 2 Roll-Up Banners:
Please use the attached resources and our site tedmpalcove.com to design two similar, but not the same banners.
Some text to use on the banner:
-Automated your marketing, grow your profits.
-Text "Vexo" to 734-555-0192 to enter to win! (this should be close to top for better viewability)
- Special packages available for this event only
- 4 must have campaigns for speakers
- Free Funnel consultations
Target Market(s)
Small businesses, speakers, consultants, etc.
Industry/Entity Type
Trade

```html
<!DOCTYPE html>
<html lang="en">
<head>
<meta charset="utf-8">
<title>Ted M Palcove Online Marketing – Roll-Up Banner</title>
<link href="https://fonts.googleapis.com/css2?family=Barlow:wght@400;500;700&family=Barlow+Semi+Condensed:wght@700&display=swap" rel="stylesheet">
<style>
  :root {
    --blue-deep: #0b5aa6;
    --blue-main: #1668b4;
    --blue-mid: #2a8fd2;
    --blue-light: #39b6ea;
    --ink: #1b1b1b;
    --white: #ffffff;
    --photo-dark: #5a5a5a;
    --photo-light: #c9c9c9;
    --badge-grey: #e4e8ec;
  }
  * { margin: 0; padding: 0; box-sizing: border-box; }
  html, body { width: 1200px; height: 2799px; overflow: hidden; background: var(--white); }
  .banner {
    position: relative; width: 1200px; height: 2799px; overflow: hidden;
    background: var(--white); font-family: "Barlow", Arial, sans-serif; color: var(--blue-main);
  }
  .top-band { position: absolute; left: 0; top: 0; width: 1200px; height: 86px; background: var(--blue-main); }
  .top-band::after { content: ""; position: absolute; left: 0; top: 56px; width: 100%; height: 22px; background: var(--blue-mid); }

  .brand-mark { position: absolute; left: 44px; top: 127px; width: 232px; height: 232px; border-radius: 50%; background: var(--blue-main); border: 6px solid #d9e6f2; }
  .brand-name { position: absolute; left: 310px; top: 150px; width: 860px; text-align: center; font-size: 132px; font-weight: 400; line-height: 1; color: var(--blue-main); }
  .brand-tagline { position: absolute; left: 330px; top: 312px; width: 810px; text-align: center; font-size: 46px; font-weight: 500; letter-spacing: 19px; color: var(--ink); }

  .headline { position: absolute; left: 47px; top: 545px; width: 1100px; font-size: 80px; font-weight: 500; line-height: 92px; color: var(--blue-main); }
  .headline span { display: block; }
  .headline .second { text-align: right; padding-right: 4px; }

  .entry-bar { position: absolute; left: 0; top: 948px; width: 1200px; height: 60px; background: var(--blue-main); }
  .entry-box {
    position: absolute; left: 121px; top: 802px; width: 958px; height: 355px; border-radius: 46px;
    background: var(--blue-main); color: var(--white); text-align: center;
    font-family: "Barlow Semi Condensed", "Arial Narrow", sans-serif; font-weight: 700;
  }
  .entry-box .lead { margin-top: 32px; font-size: 64px; line-height: 70px; }
  .entry-box .number { font-size: 138px; line-height: 136px; letter-spacing: 2px; }
  .entry-box .tail { font-size: 62px; line-height: 72px; }

  .swoosh { position: absolute; left: 0; top: 0; width: 1200px; height: 1800px; }

  .perks { position: absolute; left: 0; top: 1240px; width: 1200px; list-style: none; font-size: 50px; font-weight: 500; color: var(--blue-main); }
  .perks li { position: absolute; white-space: nowrap; }
  .perks li::before { content: "\2022"; margin-right: 14px; }
  .perks .p1 { left: 26px; top: 0; }
  .perks .p2 { left: 120px; top: 80px; }
  .perks .p3 { left: 272px; top: 160px; }

  .portrait { position: absolute; left: 285px; top: 1720px; width: 405px; height: 609px; background: linear-gradient(160deg, var(--photo-light), var(--photo-dark)); }

  .as-seen-label { position: absolute; left: 692px; top: 1720px; width: 222px; height: 34px; background: #000; color: var(--white); font-weight: 700; font-size: 31px; line-height: 34px; text-align: center; letter-spacing: 1px; }
  .press-list { position: absolute; left: 692px; top: 1770px; width: 222px; list-style: none; text-align: center; font-weight: 700; color: var(--ink); }
  .press-list li { height: 140px; display: flex; align-items: center; justify-content: center; font-size: 44px; line-height: 1; }
  .press-list li + li { margin-top: 0; }

  .partner-badge { position: absolute; top: 2351px; height: 103px; border-radius: 10px; background: var(--badge-grey); }
  .partner-badge.first { left: 168px; width: 448px; }
  .partner-badge.second { left: 733px; width: 312px; }

  .bottom-band { position: absolute; left: 0; top: 2482px; width: 1200px; height: 317px; background: var(--blue-main); }
  .bottom-band .stripe { position: absolute; left: 0; width: 100%; background: var(--blue-mid); }
  .bottom-band .stripe.upper { top: 102px; height: 18px; }
  .bottom-band .stripe.lower { top: 233px; height: 14px; }
  .site-link { position: absolute; left: 0; top: 2622px; width: 1200px; text-align: center; color: var(--white); font-size: 60px; font-weight: 400; line-height: 66px; letter-spacing: 1px; }
  .site-link svg { width: 46px; height: 46px; vertical-align: -4px; margin-right: 22px; }
</style>
</head>
<body>
<main class="banner">
  <div class="top-band"></div>

  <div class="brand-mark" role="img" aria-label="Brand portrait illustration in a blue circle"></div>
  <div class="brand-name">Ted M Palcove</div>
  <div class="brand-tagline">ONLINE MARKETING</div>

  <h1 class="headline">
    <span class="first">Automated your marketing,</span>
    <span class="second">Grow your profits.</span>
  </h1>

  <div class="entry-bar"></div>
  <div class="entry-box">
    <p class="lead">Text "Vexo" to</p>
    <p class="number">734-555-0192</p>
    <p class="tail">to enter to win!</p>
  </div>

  <svg class="swoosh" viewBox="0 0 1200 1800" aria-hidden="true">
    <path d="M0,1418 C260,1650 820,1640 1200,1232 L1200,1320 C830,1700 260,1700 0,1468 Z" fill="#39b6ea"/>
    <path d="M0,1478 C260,1708 830,1712 1200,1332 L1200,1440 C850,1770 270,1740 0,1505 Z" fill="#1f7cc6"/>
  </svg>

  <ul class="perks">
    <li class="p1">Special packages available for this event only</li>
    <li class="p2">4 must have campaigns for speakers</li>
    <li class="p3">Free Funnel consultations</li>
  </ul>

  <div class="portrait" role="img" aria-label="Black and white portrait photograph of the marketer"></div>

  <div class="as-seen-label">AS SEEN ON</div>
  <ul class="press-list">
    <li>Orbit News</li>
    <li>Kestrel</li>
    <li>Northline</li>
    <li>Vantage</li>
  </ul>

  <div class="partner-badge first" role="img" aria-label="Summit Ledger certified partner badge"></div>
  <div class="partner-badge second" role="img" aria-label="Brightwire certified partner badge"></div>

  <footer class="bottom-band">
    <div class="stripe upper"></div>
    <div class="stripe lower"></div>
  </footer>
  <p class="site-link">
    <svg viewBox="0 0 24 24" aria-hidden="true" fill="none" stroke="#ffffff" stroke-width="1.6">
      <circle cx="12" cy="12" r="9"/>
      <ellipse cx="12" cy="12" rx="4" ry="9"/>
      <line x1="3" y1="12" x2="21" y2="12"/>
    </svg>tedmpalcove.com
  </p>
</main>
</body>
</html>
```